Islamic App which helps to calculate, track and pay Zakat

We need an application which helps muslim people to calculate and pay Zakat - mandatory donations which muslim should pay based on his income. The application will consist of two parts (applications) - the one which is used by "payer" and another one - used by "receiver". To make a payment "payer" will scan QR-code which "receiver" will generate in his app and show to payer. "Receiver" will have option to initiate cash withdrawal once he collected required minimum for the withdrawal.
Important that "payer" side journey to make a payment should be as short as possible - imaging same as you make donation by cash - you just gave money and left, similar experience should be with app - couple-three taps to make it. For receiver side major requirement is to keep the UI/UX as simple as possible, these guys usually are not aware about online payments (roughly speaking this part of the app should be more similar to Lumbrela rather than to banking/financial app)
In this Figma I tried to sketch the UX for both sides (just to explain the idea): https://www.draftlynx.net/file/pkr4T8WmZtLsQbXeNcJV2a/Sketch-starter?type=design&node-id=2831-475190&mode=design

Target Market(s)

Muslims

Industry/Entity Type

Donations

Colors
0094D4
00A9DD
6FCCEA
C7EBF8
E9F6FB
00AB8E
00BBA5
67D7C9
C6EFE9
E9F9F6

Requirements
Must have
• The application should have soul. Design should show that this application intend to help people, not just money transfer
Nice to have
• Payment should be as quick as possible, in the sketches I showed it as banknotes/coins which user need to slide-up to pay. Maybe make it similar as Vexa RT dock icons?
Should not have
• The application should not look as banking/financial app or wallet app

```html
<!DOCTYPE html>
<html lang="en">
<head>
<meta charset="utf-8">
<title>Zakat App – Screens</title>
<link href="https://fonts.googleapis.com/css2?family=Poppins:wght@300;400;500;600;700;800&display=swap" rel="stylesheet">
<style>
:root{
  --blue:#0094D4;--blue-2:#00A9DD;--blue-3:#6FCCEA;--blue-4:#C7EBF8;--blue-5:#E9F6FB;
  --teal:#00AB8E;--teal-2:#00BBA5;--teal-3:#67D7C9;--teal-4:#C6EFE9;--teal-5:#E9F9F6;
  --bg-top:#1d3f78;--bg-bottom:#2a6c8e;--ink:#1b1f24;--muted:#8a9099;--field:#f1f3f6;
  --frame:#0c1016;--label:#2fb8e8;--danger:#e0413c;
}
*{box-sizing:border-box;margin:0;padding:0}
html,body{width:779px;height:1200px;overflow:hidden}
body{font-family:"Poppins",sans-serif;color:var(--ink);background:linear-gradient(170deg,var(--bg-top) 0%,#22547f 45%,var(--bg-bottom) 100%);position:relative}
.section-label{position:absolute;writing-mode:vertical-rl;transform:rotate(180deg);font-size:5px;letter-spacing:3.2px;color:var(--label);font-weight:500;white-space:nowrap}
.phone{position:absolute;width:110px;border:2.5px solid var(--frame);border-radius:14px;background:#fff;overflow:hidden}
.status{position:absolute;top:6px;left:0;right:0;height:6px;display:flex;justify-content:space-between;padding:0 12px;font-size:4px;font-weight:600;z-index:3}
.status.light{color:#fff}
.status-icons{display:flex;gap:1.5px;align-items:center}
.status-icons i{display:block;background:currentColor;border-radius:1px}
.home-bar{position:absolute;bottom:4px;left:50%;width:34px;height:1.5px;margin-left:-17px;background:var(--ink);border-radius:2px;z-index:3}
.photo{position:absolute;left:0;right:0;top:0}
.photo.payer{background:linear-gradient(180deg,#1a1a1f 0%,#35465a 30%,#2d6aa8 55%,#1c9ed6 78%,#19b0c6 100%)}
.photo.mosque{background:linear-gradient(180deg,#cfdde6 0%,#bcd3e2 35%,#7fb8dc 62%,#1d9fd8 82%,#13a9c9 100%)}
.photo.blur{background:linear-gradient(180deg,#1e1e22 0%,#4a3f3a 55%,#6b5a52 100%)}
.hero-name{position:absolute;left:8px;font-size:17px;font-weight:800;color:#fff;letter-spacing:-.3px}
.hero-sub{position:absolute;left:8px;right:10px;font-size:6px;font-weight:300;color:#fff;line-height:1.25}
.bottom-sheet{position:absolute;left:0;right:0;bottom:0;background:#fff}
.round-btn{position:absolute;border-radius:50%;background:linear-gradient(160deg,var(--blue-2),var(--blue));border:2px solid #fff;display:flex;align-items:center;justify-content:center;box-shadow:0 1px 3px rgba(0,80,140,.35)}
.tiny-caption{position:absolute;font-size:2.8px;color:var(--blue);font-weight:500;text-align:center}
.step-body{position:absolute;left:0;right:0;top:43px;bottom:0;background:#fff}
.step-bump{position:absolute;top:-8px;left:50%;width:30px;height:30px;margin-left:-15px;border-radius:50%;background:#fff}
.stepper{position:absolute;top:18px;left:14px;right:14px;height:4px}
.stepper .line{position:absolute;top:1.8px;left:4px;right:4px;height:.6px;background:#d7dbe0}
.stepper .line.on{background:var(--blue)}
.stepper .dot{position:absolute;top:0;width:4.5px;height:4.5px;border-radius:50%;border:.6px solid #9aa1aa;background:#fff;font-size:2.6px;line-height:3.3px;text-align:center;color:#666}
.stepper .dot.on{border-color:var(--blue);color:var(--blue)}
.step-labels{position:absolute;top:25px;left:6px;right:6px;display:flex;justify-content:space-between;font-size:2.8px;color:var(--muted)}
.step-labels .on{color:var(--blue)}
.title{position:absolute;left:8px;font-size:4.4px;font-weight:500}
.f-label{position:absolute;left:8px;font-size:3.1px;color:#555;letter-spacing:.1px}
.field{position:absolute;left:8px;right:8px;height:12px;background:var(--field);border-radius:2px;display:flex;justify-content:space-between;align-items:center;padding:0 4px;font-size:4.2px;font-weight:600}
.field .cur{font-size:3px;color:#9aa1aa;font-weight:400}
.field.outline{background:#fff;border:.7px solid var(--teal-3);height:16px}
.field.outline .lbl{font-size:3.4px;font-weight:400}
.field.outline small{font-size:3px;font-weight:400;color:var(--muted)}
.rule{position:absolute;left:8px;right:8px;height:.5px;background:#e1e4e8}
.total-row{position:absolute;left:8px;right:8px;display:flex;justify-content:space-between;align-items:baseline;font-size:4px}
.total-row b{font-size:5.2px;font-weight:700}
.total-row small{font-size:3px;color:var(--muted)}
.cta{position:absolute;left:8px;right:8px;height:14px;border-radius:8px;background:linear-gradient(90deg,var(--blue),var(--blue-2) 70%,var(--teal-2));color:#fff;font-size:4.4px;font-weight:500;display:flex;align-items:center;justify-content:center;gap:14px}
.keypad{position:absolute;left:0;right:0;bottom:0;background:linear-gradient(180deg,#2e8fc8 0%,#3aa6bb 40%,#3cb3a8 100%);padding:2px 1.5px;display:grid;grid-template-columns:repeat(3,1fr);grid-auto-rows:12px;gap:2px;align-content:start}
.key{background:#fff;border-radius:1.5px;display:flex;flex-direction:column;align-items:center;justify-content:center;font-size:6px;line-height:6px;color:var(--ink)}
.key small{font-size:2.3px;line-height:2.6px;letter-spacing:.4px;font-weight:600}
.key.blank{background:transparent}
.key.del{background:transparent;color:#1e3b44;font-size:5px}
.zakat-due{position:absolute;left:8px;right:8px;border:.8px solid var(--teal-2);border-radius:2px;overflow:hidden}
.zakat-due .head{background:var(--teal-2);color:#fff;font-size:3.4px;font-weight:500;text-align:center;height:7px;line-height:7px}
.zakat-due .amount{height:22px;display:flex;align-items:center;justify-content:center;color:var(--teal-2);font-size:9px;font-weight:600;gap:2px}
.zakat-due .amount small{font-size:5px;font-weight:400}
.note{position:absolute;left:8px;right:8px;display:flex;gap:3px;font-size:2.7px;color:var(--blue);line-height:1.5}
.note i{flex:none;width:5px;height:5px;border-radius:50%;background:var(--blue);color:#fff;font-style:normal;font-size:3.4px;line-height:5px;text-align:center}
.pay-sheet{position:absolute;left:0;right:0;top:99px;bottom:0;background:#fff;border-radius:3px 3px 0 0}
.pay-head{position:absolute;top:5px;left:5px;right:5px;display:flex;justify-content:space-between;align-items:center;font-size:6px;font-weight:600}
.pay-head .x{width:5px;height:5px;border-radius:50%;background:#e6e8eb;font-size:3px;line-height:5px;text-align:center;color:#666;font-weight:400}
.pay-row{position:absolute;left:4px;right:4px;background:#f6f7f9;border-radius:2px;display:flex;align-items:center;gap:3px;padding:0 4px;font-size:3.4px;line-height:1.4}
.pay-row .sub{font-size:2.6px;color:var(--muted)}
.pay-row .chev{margin-left:auto;color:#888;font-size:4px}
.chip{width:9px;height:6px;border-radius:1px;background:linear-gradient(90deg,#f5c6d6,#f1d38f,#b9e0f5)}
.pay-total{position:absolute;left:4px;right:4px;top:82px;border-top:.5px solid #e4e6e9;padding-top:3px}
.pay-total small{font-size:2.6px;color:var(--muted);display:block}
.pay-total b{font-size:7px;font-weight:500}
.amount-row{position:absolute;left:8px;display:flex;align-items:baseline;gap:2px;font-weight:700}
.amount-row small{font-weight:600;color:#9aa1aa}
.top-bar{position:absolute;top:18px;left:8px;right:8px;display:flex;align-items:center;gap:10px;font-size:4.2px;font-weight:600}
.back-btn{width:9px;height:9px;border-radius:50%;background:var(--blue);color:#fff;font-size:5px;line-height:9px;text-align:center}
.photo-card{position:absolute;left:32px;width:41px;top:37px;height:73px;border-radius:3px;overflow:hidden}
.photo-card .change{position:absolute;left:0;right:0;bottom:0;height:12px;background:#172026;color:#fff;font-size:3px;display:flex;align-items:center;justify-content:center;gap:2px}
.photo-card .change i{width:3px;height:2.5px;background:var(--teal-2);border-radius:.5px}
.textarea{position:absolute;left:8px;right:8px;height:21px;background:var(--field);border-radius:2px;padding:4px;font-size:3.6px}
.error-pill{position:absolute;left:14px;right:14px;height:9px;border-radius:2px;background:#fdecec;color:var(--danger);font-size:3.2px;display:flex;align-items:center;justify-content:center;gap:2px}
.error-pill i{width:3.6px;height:3.6px;border-radius:50%;background:var(--danger);color:#fff;font-style:normal;font-size:2.8px;line-height:3.6px;text-align:center}
.dial{position:absolute;left:0;right:0;bottom:0;height:63px;background:#eef3f7}
.dial-labels{position:absolute;top:-4px;left:6px;right:6px;display:flex;justify-content:space-between;font-size:2.6px;color:#666;line-height:1.3}
.dial-labels span:last-child{text-align:right}
.dial-numbers{position:absolute;top:26px;left:15px;right:15px;display:flex;justify-content:space-between;font-size:5px;font-weight:600}
</style>
</head>
<body>

<!-- ========== PAYER JOURNEY ========== -->
<div class="section-label" style="left:41px;top:50px">PAYER SCREEN</div>
<div class="phone" style="left:55px;top:49px;height:231px">
  <div class="photo payer" style="height:200px" role="img" aria-label="Photo of the receiver, a worker in a blue uniform and cap"></div>
  <div class="status light"><span>9:41</span><span class="status-icons"><i style="width:5px;height:3px"></i><i style="width:3px;height:3px;border-radius:50%"></i><i style="width:6px;height:3px"></i></span></div>
  <div class="hero-name" style="top:136px">Karim</div>
  <div class="hero-sub" style="top:160px">I am from Pakistan. I have three kids.</div>
  <svg style="position:absolute;left:46px;top:175px" width="12" height="10" viewBox="0 0 12 10"><path d="M1 4 L6 1 L11 4 M1 7 L6 4 L11 7 M1 10 L6 7 L11 10" stroke="#fff" stroke-width="1" fill="none" opacity=".8"/></svg>
  <div class="bottom-sheet" style="height:28px;border-radius:40px 40px 0 0"></div>
  <div class="round-btn" style="left:43px;top:188px;width:19px;height:19px">
    <svg width="9" height="9" viewBox="0 0 10 10"><rect x="1" y="2.5" width="8" height="5" rx="1" fill="none" stroke="#fff" stroke-width="1"/><circle cx="5" cy="5" r="1.2" fill="#fff"/></svg>
  </div>
  <div class="tiny-caption" style="left:0;right:0;top:211px">Swipe up to Nafa</div>
  <div class="home-bar"></div>
</div>

<div class="section-label" style="left:184px;top:50px">STEP 1: ENTER ASSET</div>
<div class="phone" style="left:199px;top:49px;height:365px">
  <div class="photo blur" style="height:50px" role="img" aria-label="Blurred photo backdrop"></div>
  <div class="status light"><span>9:41</span><span class="status-icons"><i style="width:5px;height:3px"></i><i style="width:3px;height:3px;border-radius:50%"></i><i style="width:6px;height:3px"></i></span></div>
  <div class="step-body">
    <div class="step-bump"></div>
    <div class="stepper"><div class="line"></div><span class="dot on" style="left:0">1</span><span class="dot" style="left:34px">2</span><span class="dot" style="left:68px">3</span></div>
    <div class="step-labels"><span class="on">Enter assets</span><span>Calculate Zakat</span><span>Pay</span></div>
    <div class="title" style="top:42px">Enter all the assets you own</div>
    <div class="f-label" style="top:55px">CASH AT HOME AND BANK ACCOUNTS</div>
    <div class="field" style="top:61px"><span class="cur">AED</span><span>50,500.00</span></div>
    <div class="f-label" style="top:82px">VALUE OF GOLD YOU OWN</div>
    <div class="field" style="top:88px"><span class="cur">AED</span><span>3,000.00</span></div>
    <div class="f-label" style="top:109px">VALUE OF SILVER YOU OWN</div>
    <div class="field" style="top:115px"><span class="cur">AED</span><span>2,000.00</span></div>
    <div class="f-label" style="top:136px">MONEY OWED TO YOU</div>
    <div class="field" style="top:142px"><span class="cur">AED</span><span>800.00</span></div>
    <div class="f-label" style="top:163px">OTHER ASSETS</div>
    <div class="field" style="top:169px"><span class="cur">AED</span><span>1000.00</span></div>
    <div class="rule" style="top:188px"></div>
    <div class="total-row" style="top:194px"><span>Total assets</span><span><b>58300.00</b> <small>AED</small></span></div>
    <div class="cta" style="top:214px"><span>Calculate your Zakat</span><span>→</span></div>
  </div>
  <div class="round-btn" style="left:44px;top:36px;width:17px;height:17px;border:none;color:#fff;font-size:7px">✕</div>
  <div class="keypad" style="height:78px">
    <div class="key">1</div><div class="key">2<small>ABC</small></div><div class="key">3<small>DEF</small></div>
    <div class="key">4<small>GHI</small></div><div class="key">5<small>JKL</small></div><div class="key">6<small>MNO</small></div>
    <div class="key">7<small>PQRS</small></div><div class="key">8<small>TUV</small></div><div class="key">9<small>WXYZ</small></div>
    <div class="key blank"></div><div class="key">0</div><div class="key del">⌫</div>
  </div>
  <div class="home-bar"></div>
</div>

<div class="section-label" style="left:327px;top:50px">STEP 2: CALCULATE</div>
<div class="phone" style="left:343px;top:49px;height:381px">
  <div class="photo blur" style="height:50px" role="img" aria-label="Blurred photo backdrop"></div>
  <div class="status light"><span>9:41</span><span class="status-icons"><i style="width:5px;height:3px"></i><i style="width:3px;height:3px;border-radius:50%"></i><i style="width:6px;height:3px"></i></span></div>
  <div class="step-body">
    <div class="step-bump"></div>
    <div class="stepper"><div class="line on" style="right:38px"></div><div class="line" style="left:38px"></div><span class="dot on" style="left:0">1</span><span class="dot on" style="left:34px">2</span><span class="dot" style="left:68px">3</span></div>
    <div class="step-labels"><span class="on">Enter assets</span><span class="on">Calculate Zakat</span><span>Pay</span></div>
    <div class="title" style="top:40px">Calculate your Zakat</div>
    <div class="field outline" style="top:50px"><span class="lbl">Total assets</span><span>58300.00 <small>AED</small> <span style="color:var(--teal-2)">✎</span></span></div>
    <div class="f-label" style="top:75px">EXPENSES (TAX, RENT, BILLS)</div>
    <div class="field" style="top:81px"><span class="cur">AED</span><span>30,000.00</span></div>
    <div class="f-label" style="top:102px">SHORT TERM DEBTS</div>
    <div class="field" style="top:108px"><span class="cur">AED</span><span>5,000.00</span></div>
    <div class="f-label" style="top:129px">OTHER EXPENSES</div>
    <div class="field" style="top:135px"><span class="cur">AED</span><span>10,000.00</span></div>
    <div class="rule" style="top:153px"></div>
    <div class="total-row" style="top:160px"><span>Total expenses</span><span><b>45,000.00</b> <small>AED</small></span></div>
    <div class="zakat-due" style="top:181px"><div class="head">ZAKAT DUE</div><div class="amount">332.50 <small>AED</small></div></div>
    <div class="note" style="top:219px"><i>i</i><span>If your total assets minus your total liabilities is more than $5611.84* Zakat will be obligatory on you.</span></div>
    <div class="cta" style="top:239px"><span>Pay Zakat</span><span>→</span></div>
  </div>
  <div class="round-btn" style="left:44px;top:36px;width:17px;height:17px;border:none;color:#fff;font-size:7px">←</div>
  <div class="keypad" style="height:78px">
    <div class="key">1</div><div class="key">2<small>ABC</small></div><div class="key">3<small>DEF</small></div>
    <div class="key">4<small>GHI</small></div><div class="key">5<small>JKL</small></div><div class="key">6<small>MNO</small></div>
    <div class="key">7<small>PQRS</small></div><div class="key">8<small>TUV</small></div><div class="key">9<small>WXYZ</small></div>
    <div class="key blank"></div><div class="key">0</div><div class="key del">⌫</div>
  </div>
  <div class="home-bar"></div>
</div>

<div class="section-label" style="left:470px;top:50px">STEP 3: PAY ZAKAT</div>
<div class="phone" style="left:487px;top:49px;height:276px">
  <div class="photo blur" style="height:50px" role="img" aria-label="Blurred photo backdrop"></div>
  <div class="status light"><span>9:41</span><span class="status-icons"><i style="width:5px;height:3px"></i><i style="width:3px;height:3px;border-radius:50%"></i><i style="width:6px;height:3px"></i></span></div>
  <div class="step-body">
    <div class="step-bump"></div>
    <div class="stepper"><div class="line on"></div><span class="dot on" style="left:0">1</span><span class="dot on" style="left:34px">2</span><span class="dot on" style="left:68px">3</span></div>
    <div class="step-labels"><span class="on">Enter assets</span><span class="on">Calculate Zakat</span><span class="on">Pay</span></div>
    <div class="title" style="top:40px">Pay Zakat</div>
    <div class="field outline" style="top:50px"><span class="lbl">Zakat due</span><span>332.50 <small>AED</small> <span style="color:var(--teal-2)">✎</span></span></div>
    <div class="f-label" style="top:75px">CREDIT CARD NUMBER</div>
    <div class="field" style="top:81px"><span>1080 5264 3089 7208</span><span class="cur">▭</span></div>
    <div class="f-label" style="top:102px">EXP DATE</div>
    <div class="f-label" style="top:102px;left:60px">CVV</div>
    <div class="field" style="top:108px;right:55px"><span>08/25</span></div>
    <div class="field" style="top:108px;left:60px"><span>•••</span><span style="width:4px;height:4px;border-radius:50%;background:var(--blue)"></span></div>
    <div class="cta" style="top:130px"><span>Confirm</span><span>→</span></div>
  </div>
  <div class="round-btn" style="left:44px;top:36px;width:17px;height:17px;border:none;color:#fff;font-size:7px">←</div>
  <div class="keypad" style="height:78px">
    <div class="key">1</div><div class="key">2<small>ABC</small></div><div class="key">3<small>DEF</small></div>
    <div class="key">4<small>GHI</small></div><div class="key">5<small>JKL</small></div><div class="key">6<small>MNO</small></div>
    <div class="key">7<small>PQRS</small></div><div class="key">8<small>TUV</small></div><div class="key">9<small>WXYZ</small></div>
    <div class="key blank"></div><div class="key">0</div><div class="key del">⌫</div>
  </div>
  <div class="home-bar"></div>
</div>

<div class="section-label" style="left:613px;top:50px">CONFIRMATION</div>
<div class="phone" style="left:631px;top:49px;height:231px">
  <div class="photo blur" style="height:100px" role="img" aria-label="Blurred photo backdrop"></div>
  <div class="status light"><span>9:41</span><span class="status-icons"><i style="width:5px;height:3px"></i><i style="width:3px;height:3px;border-radius:50%"></i><i style="width:6px;height:3px"></i></span></div>
  <div style="position:absolute;right:5px;top:50px;font-size:4.6px;color:#fff;text-align:right;line-height:1.3">Double Click<br>to Pay</div>
  <div style="position:absolute;right:0;top:42px;width:1.5px;height:28px;background:#fff"></div>
  <div class="pay-sheet">
    <div class="pay-head"><span>QuickPay</span><span class="x">✕</span></div>
    <div class="pay-row" style="top:16px;height:23px"><span class="chip"></span><span>Orbit Card<br><span class="sub">12 Cedar Row Lakeside<br>•••• 1234</span></span><span class="chev">›</span></div>
    <div class="pay-row" style="top:42px;height:25px"><span style="font-size:4px">●</span><span><span class="sub">Contact</span><br>r.vale@haldenworks.net<br>(555) 010-2471</span><span class="chev">›</span></div>
    <div class="pay-row" style="top:70px;height:6px;font-size:2.6px;color:var(--muted)">Shipping</div>
    <div class="pay-total"><small>Pay Halden Works</small><b>$332.50</b><span style="position:absolute;right:2px;top:6px;color:#888;font-size:4px">›</span></div>
    <div style="position:absolute;left:0;right:0;top:102px;border-top:.5px solid #e4e6e9"></div>
    <svg style="position:absolute;left:49px;top:104px" width="8" height="8" viewBox="0 0 8 8"><circle cx="4" cy="4" r="3.3" fill="none" stroke="var(--blue)" stroke-width=".6"/><path d="M4 2v4M2.8 3.2 4 2 5.2 3.2" stroke="var(--blue)" stroke-width=".6" fill="none"/></svg>
    <div style="position:absolute;left:0;right:0;top:113px;text-align:center;font-size:3px">Confirm with Side Button</div>
  </div>
  <div class="home-bar"></div>
</div>

<!-- ========== FEATURE PAIR ========== -->
<div class="phone" style="left:258px;top:525px;height:231px;transform:scale(1.15);transform-origin:top left">
  <div class="photo payer" style="height:200px" role="img" aria-label="Photo of the receiver, a worker in a blue uniform and cap"></div>
  <div class="status light"><span>9:41</span><span class="status-icons"><i style="width:5px;height:3px"></i><i style="width:3px;height:3px;border-radius:50%"></i><i style="width:6px;height:3px"></i></span></div>
  <div class="hero-name" style="top:136px">Karim</div>
  <div class="hero-sub" style="top:160px">I am from Pakistan. I have three kids.</div>
  <svg style="position:absolute;left:46px;top:175px" width="12" height="10" viewBox="0 0 12 10"><path d="M1 4 L6 1 L11 4 M1 7 L6 4 L11 7 M1 10 L6 7 L11 10" stroke="#fff" stroke-width="1" fill="none" opacity=".8"/></svg>
  <div class="bottom-sheet" style="height:28px;border-radius:40px 40px 0 0"></div>
  <div class="round-btn" style="left:43px;top:188px;width:19px;height:19px">
    <svg width="9" height="9" viewBox="0 0 10 10"><rect x="1" y="2.5" width="8" height="5" rx="1" fill="none" stroke="#fff" stroke-width="1"/><circle cx="5" cy="5" r="1.2" fill="#fff"/></svg>
  </div>
  <div class="tiny-caption" style="left:0;right:0;top:211px">Swipe up to Nafa</div>
  <div class="home-bar"></div>
</div>

<div class="phone" style="left:405px;top:525px;height:231px;transform:scale(1.15);transform-origin:top left">
  <div class="photo mosque" style="height:198px" role="img" aria-label="Photo of a white mosque dome and minaret against a pale sky"></div>
  <div class="status"><span>9:41</span><span class="status-icons"><i style="width:5px;height:3px"></i><i style="width:3px;height:3px;border-radius:50%"></i><i style="width:6px;height:3px"></i></span></div>
  <div class="round-btn" style="left:7px;top:18px;width:12px;height:12px;border:none;color:#fff;font-size:5px">✎</div>
  <div class="hero-name" style="top:136px">Karim</div>
  <div class="hero-sub" style="top:160px">I am from Pakistan. I have three kids.</div>
  <div class="bottom-sheet" style="height:36px;border-radius:0 60px 0 0"></div>
  <div class="amount-row" style="top:200px;font-size:12px">840 <small style="font-size:6px">AED</small></div>
  <div class="round-btn" style="left:67px;top:187px;width:18px;height:18px">
    <svg width="8" height="8" viewBox="0 0 8 8"><rect x="1" y="1" width="6" height="6" rx="1" fill="none" stroke="#fff" stroke-width=".8"/><path d="M4 2.5v3M2.8 4.3 4 5.5 5.2 4.3" stroke="#fff" stroke-width=".8" fill="none"/></svg>
  </div>
  <div class="tiny-caption" style="left:58px;width:36px;top:210px">Withdraw Funds</div>
  <div class="home-bar"></div>
</div>

<!-- ========== RECEIVER JOURNEY ========== -->
<div class="section-label" style="left:179px;top:882px">RECEIVER SCREEN</div>
<div class="phone" style="left:193px;top:880px;height:229px">
  <div class="photo mosque" style="height:196px" role="img" aria-label="Photo of a white mosque dome and minaret against a pale sky"></div>
  <div class="status"><span>9:41</span><span class="status-icons"><i style="width:5px;height:3px"></i><i style="width:3px;height:3px;border-radius:50%"></i><i style="width:6px;height:3px"></i></span></div>
  <div class="round-btn" style="left:7px;top:18px;width:12px;height:12px;border:none;color:#fff;font-size:5px">✎</div>
  <div class="hero-name" style="top:134px">Karim</div>
  <div class="hero-sub" style="top:158px">I am from Pakistan. I have three kids.</div>
  <div class="bottom-sheet" style="height:36px;border-radius:0 60px 0 0"></div>
  <div class="amount-row" style="top:198px;font-size:12px">840 <small style="font-size:6px">AED</small></div>
  <div class="round-btn" style="left:66px;top:185px;width:18px;height:18px">
    <svg width="8" height="8" viewBox="0 0 8 8"><rect x="1" y="1" width="6" height="6" rx="1" fill="none" stroke="#fff" stroke-width=".8"/><path d="M4 2.5v3M2.8 4.3 4 5.5 5.2 4.3" stroke="#fff" stroke-width=".8" fill="none"/></svg>
  </div>
  <div class="tiny-caption" style="left:57px;width:36px;top:208px">Withdraw Funds</div>
  <div class="home-bar"></div>
</div>

<div class="section-label" style="left:327px;top:882px">EDIT RECEIVER INFO</div>
<div class="phone" style="left:342px;top:880px;height:229px">
  <div class="status"><span>9:41</span><span class="status-icons"><i style="width:5px;height:3px"></i><i style="width:3px;height:3px;border-radius:50%"></i><i style="width:6px;height:3px"></i></span></div>
  <div class="top-bar"><span class="back-btn">←</span><span>Edit profile</span></div>
  <div class="photo-card">
    <div class="photo mosque" style="height:100%" role="img" aria-label="Profile photo of a mosque dome and minaret"></div>
    <div class="change"><i></i>Change photo</div>
  </div>
  <div class="f-label" style="top:119px">ENTER YOUR NAME</div>
  <div class="field" style="top:125px;justify-content:flex-start;gap:3px;font-size:4px"><span class="cur">●</span><span>Karim</span></div>
  <div class="f-label" style="top:148px">SHORT INFO ABOUT YOURSELF</div>
  <div class="textarea" style="top:154px">I am from Pakistan. I have three kids.</div>
  <div class="cta" style="top:188px;gap:0">Save changes</div>
  <div class="home-bar"></div>
</div>

<div class="section-label" style="left:476px;top:882px">WITHDRAW SCREEN</div>
<div class="phone" style="left:489px;top:880px;height:229px">
  <div class="status"><span>9:41</span><span class="status-icons"><i style="width:5px;height:3px"></i><i style="width:3px;height:3px;border-radius:50%"></i><i style="width:6px;height:3px"></i></span></div>
  <div class="top-bar"><span class="back-btn">←</span><span>Withdraw funds</span></div>
  <div class="amount-row" style="top:60px;left:0;right:0;justify-content:center;font-size:18px;letter-spacing:-.5px">1500 <small style="font-size:8px">AED</small></div>
  <div class="error-pill" style="top:84px"><i>!</i>Your withdrawal limit is 840 AED</div>
  <div class="dial">
    <div class="dial-labels"><span>WITHDRAWAL LIMIT<br>840 AED</span><span>MULTIPLES OF<br>100 AED</span></div>
    <svg style="position:absolute;left:0;top:0" width="105" height="50" viewBox="0 0 105 50">
      <path d="M0 0 H38 C45 0 47 6 52.5 6 C58 6 60 0 67 0 H105 V-2 H0Z" fill="#fff"/>
      <path d="M50 7 L55 7 L52.5 10Z" fill="var(--blue)"/>
      <g stroke="#aeb8c2" stroke-width=".4">
        <path d="M5 14v3M11 14v2M17 14v3M23 14v2M29 14v3M35 14v2M41 14v3M47 14v2M58 14v2M64 14v3M70 14v2M76 14v3M82 14v2M88 14v3M94 14v2M100 14v3"/>
        <path d="M5 42v2M11 42v3M17 42v2M23 42v3M29 42v2M35 42v3M41 42v2M47 42v3M53 42v2M58 42v3M64 42v2M70 42v3M76 42v2M82 42v3M88 42v2M94 42v3M100 42v2"/>
      </g>
      <path d="M52.5 13v5" stroke="var(--blue)" stroke-width=".6"/>
    </svg>
    <div class="dial-numbers"><span>1000</span><span>1500</span><span>2000</span></div>
  </div>
  <div class="home-bar"></div>
</div>

</body>
</html>
```